Need a Facebook image for childcare advertisement

We are after a design for Facebook advertisement for childcare and kindergarten centre enrolments for 2023.

I have attached a previous flyer that we have in pdf format. The new logo is also attached with this brief.

All other information is still current as per the attached flyer.

You can use same colours as per attached flyer. I will also attached some stock images that you can select to use for the design.

our website for your reference:

https://tolvenbrook.com.au

```html
<!DOCTYPE html>
<html lang="en">
<head>
<meta charset="utf-8">
<title>Tolvenbrook – 2023 enrolments now open</title>
<link rel="stylesheet" href="https://fonts.googleapis.com/css2?family=Gochi+Hand&display=swap">
<style>
  :root {
    --board: #2a2a2a;
    --chalk: #bfe4f0;
    --white: #ffffff;
    --tone-cream: #efe2d2;
    --tone-skin: #e6bf9c;
    --tone-warm: #c98f5e;
    --tone-red: #d9623e;
    --tone-blue: #6f93c2;
    --tone-stripe: #9fb6cf;
    --tone-leaf: #b7cc62;
    --tone-grass: #8fae4a;
    --tone-sun: #e9c46a;
    --tone-navy: #3b4a5e;
    --tone-slate: #8ea2b4;
    --tone-pink: #f0b8c4;
    --tone-mint: #9fd8d2;
  }
  * { margin: 0; padding: 0; box-sizing: border-box; }
  html, body {
    width: 1200px; height: 628px; overflow: hidden;
    background: var(--board);
  }
  .ad {
    position: relative; width: 1200px; height: 628px;
    background: var(--board);
    font-family: "Gochi Hand", cursive;
    color: var(--chalk);
  }
  .frame, .gallery { position: absolute; inset: 0; }
  .brand {
    position: absolute; left: 86px; top: 84px; width: 280px;
    text-align: center; color: var(--white);
  }
  .brand-name { display: block; font-size: 50px; line-height: 1; }
  .brand-tag { display: block; margin-top: 18px; font-size: 15px; letter-spacing: 0.4px; }
  .headline {
    position: absolute; left: 388px; top: 98px; width: 724px;
    font-size: 60px; line-height: 1; font-weight: 400;
    text-align: center; letter-spacing: 1.5px; white-space: nowrap;
  }
  .tagline {
    position: absolute; left: 80px; top: 490px; width: 1060px;
    text-align: center; font-size: 31px; line-height: 39px;
  }
</style>
</head>
<body>
<main class="ad">
  <svg class="frame" width="1200" height="628" viewBox="0 0 1200 628" fill="none" stroke="var(--chalk)" stroke-linecap="round">
    <path d="M22 44 C300 24 700 58 1168 20 C1174 200 1184 420 1172 602 C800 592 400 616 40 600 C48 420 26 220 22 44 Z" stroke-width="2"/>
    <path d="M34 54 C320 40 760 64 1156 34 C1164 220 1168 430 1160 592 C780 584 380 604 52 590 C58 410 36 230 34 54 Z" stroke-width="1.5"/>
    <path d="M44 70 C50 250 40 420 56 582" stroke-width="1.2"/>
  </svg>

  <div class="brand">
    <span class="brand-name">Tolvenbrook</span>
    <span class="brand-tag">EARLY CHILDHOOD LEARNING CENTRE</span>
  </div>

  <h1 class="headline">2023 enrolments now open</h1>

  <svg class="gallery" width="1200" height="628" viewBox="0 0 1200 628">
    <defs>
      <linearGradient id="tone-play" x1="0" y1="0" x2="0.6" y2="1">
        <stop offset="0" stop-color="var(--tone-cream)"/>
        <stop offset="0.45" stop-color="var(--tone-skin)"/>
        <stop offset="0.75" stop-color="var(--tone-red)"/>
        <stop offset="1" stop-color="var(--tone-blue)"/>
      </linearGradient>
      <linearGradient id="tone-blocks" x1="0" y1="0" x2="1" y2="1">
        <stop offset="0" stop-color="var(--tone-cream)"/>
        <stop offset="0.4" stop-color="var(--tone-warm)"/>
        <stop offset="0.7" stop-color="var(--tone-stripe)"/>
        <stop offset="1" stop-color="var(--tone-sun)"/>
      </linearGradient>
      <linearGradient id="tone-outdoor" x1="0" y1="0" x2="1" y2="1">
        <stop offset="0" stop-color="var(--tone-sun)"/>
        <stop offset="0.35" stop-color="var(--tone-leaf)"/>
        <stop offset="0.65" stop-color="var(--tone-skin)"/>
        <stop offset="1" stop-color="var(--tone-grass)"/>
      </linearGradient>
      <linearGradient id="tone-writing" x1="0" y1="0" x2="0" y2="1">
        <stop offset="0" stop-color="var(--tone-slate)"/>
        <stop offset="0.4" stop-color="var(--tone-skin)"/>
        <stop offset="0.75" stop-color="var(--tone-navy)"/>
        <stop offset="1" stop-color="var(--tone-cream)"/>
      </linearGradient>
      <linearGradient id="tone-reading" x1="0" y1="0" x2="1" y2="1">
        <stop offset="0" stop-color="var(--tone-leaf)"/>
        <stop offset="0.35" stop-color="var(--tone-skin)"/>
        <stop offset="0.7" stop-color="var(--tone-pink)"/>
        <stop offset="1" stop-color="var(--tone-mint)"/>
      </linearGradient>
    </defs>
    <g role="img" aria-label="Photo of a toddler stacking colourful building bricks">
      <circle cx="192" cy="349" r="82" fill="url(#tone-play)"/>
    </g>
    <g role="img" aria-label="Photo of two children building a tower of wooden blocks">
      <circle cx="398" cy="349" r="84" fill="url(#tone-blocks)"/>
    </g>
    <g role="img" aria-label="Photo of a child and carer eating apples outdoors">
      <circle cx="593" cy="354" r="84" fill="url(#tone-outdoor)"/>
    </g>
    <g role="img" aria-label="Photo of a boy writing with a pencil at a table">
      <circle cx="800" cy="350" r="84" fill="url(#tone-writing)"/>
    </g>
    <g role="img" aria-label="Photo of an educator reading with two girls">
      <circle cx="1007" cy="350" r="84" fill="url(#tone-reading)"/>
    </g>
    <g fill="none" stroke="var(--chalk)" stroke-width="2.2">
      <circle cx="192" cy="349" r="86"/><circle cx="189" cy="352" r="91" stroke-width="1.3"/>
      <circle cx="398" cy="349" r="87"/><circle cx="401" cy="346" r="92" stroke-width="1.3"/>
      <circle cx="593" cy="354" r="87"/><circle cx="590" cy="357" r="92" stroke-width="1.3"/>
      <circle cx="800" cy="350" r="87"/><circle cx="803" cy="347" r="92" stroke-width="1.3"/>
      <circle cx="1007" cy="350" r="87"/><circle cx="1004" cy="353" r="92" stroke-width="1.3"/>
    </g>
  </svg>

  <p class="tagline">We offer a great atmosphere for the children to explore the world around them<br>and take part in the school readiness program.</p>
</main>
</body>
</html>
```